Lotus Leaf Kitchen Road Billboard

Road Billboard I need all of this information on it
Authentic Thai Food Bangkok Style
6.5 Miles on the right
4126 Maple Ridge Rd Otto NC
828-555-4172

```html
<!DOCTYPE html>
<html lang="en">
<head>
<meta charset="utf-8">
<title>Lotus Leaf Kitchen – Road Billboard</title>
<link rel="stylesheet" href="https://fonts.googleapis.com/css2?family=Bebas+Neue&family=Poppins:wght@400;600;700&display=swap">
<style>
  :root {
    --ink: #000000;
    --gold: #d6a916;
    --white: #ffffff;
    --outline: #2b2b2b;
    --page: #ffffff;
    --flame: #c9561a;
    --ember: #7a2a0c;
  }
  html, body {
    margin: 0;
    width: 951px;
    height: 1200px;
    overflow: hidden;
    background: var(--page);
  }
  .billboard {
    position: absolute;
    left: 30px;
    top: 346px;
    width: 891px;
    height: 507px;
    background: var(--ink);
    overflow: hidden;
  }
  .food-photo {
    position: absolute;
    left: 470px;
    top: 0;
    width: 421px;
    height: 400px;
    background:
      radial-gradient(ellipse 55% 45% at 70% 35%, #6d7a3a 0%, #4a3a1c 35%, transparent 70%),
      radial-gradient(ellipse 50% 35% at 55% 82%, var(--flame) 0%, var(--ember) 40%, transparent 75%),
      radial-gradient(ellipse 40% 50% at 95% 30%, #d9782a 0%, transparent 70%);
    background-color: #1a120c;
  }
  .food-photo::after {
    content: "";
    position: absolute;
    inset: 0;
    background: linear-gradient(90deg, var(--ink) 0%, rgba(0,0,0,0.6) 20%, rgba(0,0,0,0) 45%);
  }
  .headline {
    position: absolute;
    left: 27px;
    top: 25px;
    margin: 0;
    font-family: "Bebas Neue", "Oswald", sans-serif;
    font-weight: 400;
    font-size: 108px;
    line-height: 104px;
    letter-spacing: -1px;
    color: var(--gold);
    text-transform: uppercase;
    white-space: nowrap;
    text-shadow:
      2px 2px 0 var(--outline), -2px -2px 0 var(--outline),
      2px -2px 0 var(--outline), -2px 2px 0 var(--outline);
  }
  .headline span { display: block; }
  .brand-name {
    position: absolute;
    left: 423px;
    top: 160px;
    width: 220px;
    text-align: center;
    font-family: "Poppins", sans-serif;
    font-weight: 600;
    font-size: 20px;
    line-height: 30px;
    white-space: nowrap;
    color: var(--white);
    margin: 0;
  }
  .shapes {
    position: absolute;
    inset: 0;
  }
  .address {
    position: absolute;
    left: 84px;
    top: 360px;
    margin: 0;
    font-family: "Poppins", sans-serif;
    font-weight: 400;
    font-size: 25px;
    line-height: 36px;
    white-space: nowrap;
    color: var(--white);
  }
  .directions {
    position: absolute;
    left: 33px;
    top: 450px;
    margin: 0;
    font-family: "Poppins", sans-serif;
    font-weight: 700;
    font-size: 30px;
    letter-spacing: -0.8px;
    line-height: 40px;
    white-space: nowrap;
    color: var(--ink);
  }
  .phone {
    position: absolute;
    left: 541px;
    top: 428px;
    margin: 0;
    font-family: "Bebas Neue", "Oswald", sans-serif;
    font-weight: 400;
    font-size: 78px;
    line-height: 78px;
    letter-spacing: 0;
    white-space: nowrap;
    color: var(--ink);
  }
</style>
</head>
<body>
  <section class="billboard">
    <div class="food-photo" role="img" aria-label="Shrimp and vegetables tossed over a flaming wok with sparks"></div>

    <svg class="shapes" width="891" height="507" viewBox="0 0 891 507" aria-hidden="true">
      <polygon class="band-directions" points="0,433 460,433 399,507 0,507" fill="var(--gold)"/>
      <polygon class="band-phone" points="487,399 891,399 891,507 399,507" fill="var(--white)"/>
      <g class="icon-pin" fill="var(--gold)">
        <path d="M49 356c-10 0-17 8-17 17 0 12 17 28 17 28s17-16 17-28c0-9-7-17-17-17zm0 24a7 7 0 1 1 0-14 7 7 0 0 1 0 14z"/>
        <ellipse cx="49" cy="404" rx="14" ry="4" fill="none" stroke="var(--gold)" stroke-width="3"/>
      </g>
      <g class="icon-phone" fill="var(--ink)">
        <path d="M486 436c-4 3-6 9-3 17 4 11 13 22 24 27 6 3 12 2 15-2l3-4c1-2 1-4-1-5l-8-6c-2-1-4-1-5 1l-3 3c-6-3-11-9-13-15l3-2c2-2 2-4 1-5l-5-9c-1-2-3-2-5-1z"/>
        <path d="M503 432a16 16 0 0 1 14 14" fill="none" stroke="var(--ink)" stroke-width="3" stroke-linecap="round"/>
        <path d="M504 424a24 24 0 0 1 21 21" fill="none" stroke="var(--ink)" stroke-width="3" stroke-linecap="round"/>
      </g>
    </svg>

    <h1 class="headline">
      <span>Authentic</span>
      <span>Thai Food</span>
      <span>Bangkok Style</span>
    </h1>

    <p class="brand-name">Lotus Leaf Kitchen</p>

    <p class="address">4126 Maple Ridge Rd Otto NC</p>
    <p class="directions">6.5 MILES ON THE RIGHT</p>
    <p class="phone">828-555-4172</p>
  </section>
</body>
</html>
```